Korvane Design Template

I'd like to have a powerpoint templates. In particular a resume template design upon the Korvane website (www.korvane.nl). Korvane is the overarching label in grey tones. The website is therefore more focussed on Techkorvane in blue colors, I expect more korvanes in the future with different color tones.

The resume template can hopefulle reused as template for business development and more.

The template should be highly professional. Preferably with a one-pager summary in front and 2 work experience details and last page with education/certificates and competences.

The onepager master slide should include
- Profile picture
- Name
- About me (optionally to mention this literally, this text can be alongside/next to the profile picture
- Table of work experience summary

In short, age, place of living, mobile phone nr in footer?
In the workexperience it describes Role, timeframe, subtitle used in slide 1 (summary of role), with a section of scope and section for achievements.

From a visual perspective, please stick to the logos provided. You may want to grey out the logo. Keep the logo as it is and work with collor pallet
Light Grey: #DEDEDE
Medium Grey: #888888
Black: #3A3A3A

```html
<!DOCTYPE html>
<html lang="en">
<head>
<meta charset="utf-8">
<title>Korvane Resume Template – Dark version</title>
<link href="https://fonts.googleapis.com/css2?family=Poppins:wght@400;500;600;700&display=swap" rel="stylesheet">
<style>
  :root{
    --blue:#1976d2;
    --blue-soft:#cfe2f5;
    --black:#3A3A3A;
    --ink:#2b2b2b;
    --panel:#454545;
    --panel-dark:#272727;
    --medium:#888888;
    --light:#DEDEDE;
    --white:#ffffff;
    --text:#e4e4e4;
  }
  *{box-sizing:border-box;margin:0;padding:0}
  html,body{width:1200px;height:3757px;overflow:hidden;background:var(--white);font-family:"Poppins",sans-serif;color:var(--white)}
  .page-title{position:absolute;left:41px;top:48px;font-size:50px;font-weight:400;color:var(--blue);letter-spacing:.5px}
  .side-label{position:absolute;font-size:38px;color:#111;transform:translate(-50%,-50%) rotate(-90deg);white-space:nowrap}
  .slide{position:absolute;left:147px;width:942px;height:529px;background:var(--black);overflow:hidden;box-shadow:0 16px 22px rgba(0,0,0,.35)}
  .abs{position:absolute}
  .wordmark{position:absolute;font-weight:400;color:var(--white);white-space:nowrap;line-height:1}
  .photo{position:absolute;border-radius:50%;border:5px solid var(--white);background:radial-gradient(circle at 50% 40%,#c9a58e 0,#a98470 38%,#dcdcdc 40%,#f2f2f2 100%);box-shadow:0 0 0 7px var(--blue)}
  .name{position:absolute;color:var(--blue);font-weight:700;font-size:35px;line-height:42px;text-transform:uppercase;white-space:nowrap}
  .role{position:absolute;font-size:16px;color:var(--white)}
  .socials{position:absolute;display:flex;gap:10px}
  .socials i{width:17px;height:17px;border-radius:50%;background:var(--blue);display:block}
  .dash{position:absolute;height:3px;background:var(--medium)}
  .hello{position:absolute;font-size:21px;color:var(--white);border-bottom:0}
  .hello-rule{position:absolute;height:3px;width:42px;background:var(--medium)}
  .card{position:absolute;background:var(--panel);border-radius:5px}
  .card-head{position:absolute;left:9px;right:9px;top:9px;height:30px;background:var(--panel-dark);border-radius:3px;font-size:17px;font-weight:600;line-height:30px;padding-left:10px;color:var(--white)}
  .card-title{position:absolute;color:var(--blue);font-size:18px;font-weight:500}
  .body{position:absolute;font-size:11px;line-height:18px;color:var(--text)}
  .blue{color:var(--blue)}
  .small-blue{font-size:11px;color:var(--blue)}
  .year{font-size:11px;font-weight:600;color:var(--white)}
  .bullet{position:absolute;font-size:11px;line-height:18px;color:var(--text);padding-left:13px}
  .bullet::before{content:"•";position:absolute;left:0;top:-1px;color:var(--blue)}
  .skill{position:absolute}
  .skill-row{display:flex;justify-content:space-between;font-size:11px;color:var(--white)}
  .skill-row .pct{color:var(--blue)}
  .track{position:relative;height:3px;background:var(--white);margin-top:5px;border-radius:2px}
  .track i{position:absolute;left:0;top:0;bottom:0;background:var(--blue);border-radius:2px}
  .track i::after{content:"";position:absolute;right:-4px;top:-3px;width:9px;height:9px;border-radius:50%;background:var(--white);border:2px solid var(--blue)}
  .skill.big .skill-row{font-size:13px}
  .hobbies{position:absolute;display:flex}
  .hobby{display:flex;flex-direction:column;align-items:center;gap:4px;font-size:11px;color:var(--white);border-right:1px solid var(--medium)}
  .hobby:last-child{border-right:0}
  .hobby svg{width:18px;height:18px;fill:none;stroke:var(--blue);stroke-width:1.6}
  .slide-footer{position:absolute;left:0;right:0;bottom:0;height:36px;background:var(--light)}
  .contact{position:absolute;top:5px;display:flex;align-items:center;gap:9px;color:#222}
  .contact .ico{width:27px;height:27px;border-radius:50%;background:var(--blue);display:flex;align-items:center;justify-content:center}
  .contact .ico svg{width:15px;height:15px;fill:var(--white)}
  .contact b{display:block;font-size:9.5px;font-weight:600;line-height:11px}
  .contact span{display:block;font-size:8.5px;line-height:10px}
  .donut{position:absolute;width:72px;text-align:center}
  .donut svg{width:72px;height:72px}
  .donut .val{position:absolute;left:0;right:0;top:24px;font-size:15px;font-weight:600;color:var(--white)}
  .donut .cap{font-size:10px;color:var(--white);margin-top:2px}
  .vline{position:absolute;width:1px;background:var(--medium)}
</style>
</head>
<body>

<svg width="0" height="0" style="position:absolute">
  <defs>
    <symbol id="pin" viewBox="0 0 24 24"><path d="M12 2a7 7 0 0 0-7 7c0 5 7 13 7 13s7-8 7-13a7 7 0 0 0-7-7zm0 9.5a2.5 2.5 0 1 1 0-5 2.5 2.5 0 0 1 0 5z"/></symbol>
    <symbol id="phone" viewBox="0 0 24 24"><path d="M6.6 10.8a15 15 0 0 0 6.6 6.6l2.2-2.2a1 1 0 0 1 1-.25 11 11 0 0 0 3.6.6 1 1 0 0 1 1 1V20a1 1 0 0 1-1 1A17 17 0 0 1 3 4a1 1 0 0 1 1-1h3.5a1 1 0 0 1 1 1c0 1.25.2 2.45.6 3.6a1 1 0 0 1-.25 1z"/></symbol>
    <symbol id="mail" viewBox="0 0 24 24"><path d="M3 5h18v14H3z M3 6l9 7 9-7" fill="none" stroke="#fff" stroke-width="2"/></symbol>
    <symbol id="pen" viewBox="0 0 24 24"><path d="M5 3h10l4 4v14H5z M9 15l6-6 2 2-6 6H9z"/></symbol>
    <symbol id="film" viewBox="0 0 24 24"><path d="M3 10h18v10H3z M3 10l16-5 1 3 M8 8.5l2 2.5 M13 7l2 2.5"/></symbol>
    <symbol id="ball" viewBox="0 0 24 24"><circle cx="12" cy="12" r="8"/><path d="M4 12h16 M12 4v16 M6 6l12 12 M18 6 6 18"/></symbol>
    <symbol id="book" viewBox="0 0 24 24"><path d="M3 5h7a2 2 0 0 1 2 2v13a2 2 0 0 0-2-2H3z M21 5h-7a2 2 0 0 0-2 2v13a2 2 0 0 1 2-2h7z"/></symbol>
  </defs>
</svg>

<h1 class="page-title">Dark version</h1>
<div class="side-label" style="left:70px;top:372px">Front 1</div>
<div class="side-label" style="left:61px;top:955px">Front 2</div>

<!-- Cover dark -->
<section class="slide cover-dark" style="top:131px">
  <div class="abs" role="img" aria-label="Dimmed photo of an office interior" style="inset:0;background:radial-gradient(ellipse at 30% 40%,#4a4a4a 0,#383838 55%,#333 100%)"></div>
  <div class="wordmark" style="left:0;right:0;top:38px;text-align:center;font-size:58px">korvane</div>
  <div class="photo" role="img" aria-label="Profile portrait" style="left:390px;top:158px;width:180px;height:180px"></div>
  <div class="abs" style="left:0;right:0;top:388px;text-align:center;font-size:44px;font-weight:700">RESUME TEMPLATE</div>
  <div class="abs" style="left:0;right:0;top:445px;text-align:center;font-size:29px;font-weight:600">FOR <span class="blue">KORVANE</span></div>
</section>

<!-- Cover light -->
<section class="slide cover-light" style="top:725px;background:var(--white)">
  <div class="abs" style="left:0;right:0;top:0;height:168px;background:linear-gradient(180deg,#ffffff 0,var(--blue-soft) 100%)"></div>
  <div class="abs" style="left:0;right:0;top:168px;height:252px;background:var(--black)"></div>
  <div class="abs" style="left:79px;top:46px;font-size:27px;font-weight:500;color:var(--black)">TECH</div>
  <div class="wordmark" style="left:76px;top:75px;font-size:72px;color:var(--black)">korvane</div>
  <div class="abs" style="left:82px;top:233px;font-size:44px;font-weight:700">RESUME TEMPLATE</div>
  <div class="abs" style="left:82px;top:290px;font-size:29px;font-weight:600">FOR <span class="blue">KORVANE</span></div>
  <div class="abs" role="img" aria-label="Blue tinted photo of a city" style="left:540px;top:82px;width:350px;height:350px;border-radius:50%;background:radial-gradient(circle at 40% 45%,#5aa0e6 0,#1976d2 55%,#0f5aa8 100%)"></div>
</section>

<!-- One-pager -->
<section class="slide onepager" style="top:1318px">
  <div class="abs" style="left:0;top:0;width:303px;bottom:0;background:var(--ink)"></div>
  <div class="wordmark" style="left:71px;top:24px;font-size:28px">korvane</div>
  <div class="photo" role="img" aria-label="Profile portrait" style="left:53px;top:93px;width:130px;height:130px"></div>
  <div class="dash" style="left:44px;top:261px;width:42px"></div>
  <div class="name" style="left:43px;top:271px">Aldric<br>Venn</div>
  <div class="role" style="left:45px;top:360px">Korvane Lead</div>
  <div class="socials" style="left:49px;top:392px" aria-label="Social profiles"><i></i><i></i><i></i></div>

  <div class="card" style="left:310px;top:30px;width:617px;height:95px">
    <div class="card-title" style="left:16px;top:8px">About Me</div>
    <div class="body" style="left:16px;top:36px;width:585px">Lorem ipsum dolor sit amet, consectetuer adipiscing elit. Maecenas porttitor congue massa. Fusce posuere, magna sed pulvinar ultricies, purus lectus malesuada libero, sit amet</div>
  </div>

  <div class="card" style="left:310px;top:136px;width:617px;height:194px">
    <div class="card-head">Work Experience</div>
    <div class="vline" style="left:131px;top:56px;height:128px"></div>
    <div class="vline" style="left:277px;top:56px;height:128px"></div>
    <div class="abs year" style="left:16px;top:58px">Year 2018</div>
    <div class="abs small-blue" style="left:141px;top:58px">Company Name</div>
    <div class="body" style="left:288px;top:58px;width:300px">Lorem ipsum dolor sit amet, consectetuer adipiscing elit.</div>
    <div class="abs year" style="left:16px;top:103px">Year 2020</div>
    <div class="abs small-blue" style="left:141px;top:103px">Company Name</div>
    <div class="body" style="left:288px;top:103px;width:300px">Lorem ipsum dolor sit amet, consectetuer adipiscing elit.</div>
    <div class="abs year" style="left:16px;top:148px">Year 2024</div>
    <div class="abs small-blue" style="left:141px;top:148px">Company Name</div>
    <div class="body" style="left:288px;top:148px;width:300px">Lorem ipsum dolor sit amet, consectetuer adipiscing elit.</div>
  </div>

  <div class="card" style="left:310px;top:340px;width:276px;height:143px">
    <div class="card-head">Hobbies</div>
    <div class="hobbies" style="left:8px;top:62px;width:260px">
      <div class="hobby" style="width:65px"><svg><use href="#pen"/></svg>Writing</div>
      <div class="hobby" style="width:65px"><svg><use href="#film"/></svg>Movies</div>
      <div class="hobby" style="width:65px"><svg><use href="#ball"/></svg>Sport</div>
      <div class="hobby" style="width:65px"><svg><use href="#book"/></svg>Reading</div>
    </div>
  </div>

  <div class="card" style="left:597px;top:340px;width:330px;height:143px">
    <div class="card-head">Skill</div>
    <div class="skill" style="left:14px;right:14px;top:48px"><div class="skill-row"><span>Skill 1</span><span class="pct">70%</span></div><div class="track"><i style="width:70%"></i></div></div>
    <div class="skill" style="left:14px;right:14px;top:77px"><div class="skill-row"><span>Skill 2</span><span class="pct">50%</span></div><div class="track"><i style="width:50%"></i></div></div>
    <div class="skill" style="left:14px;right:14px;top:105px"><div class="skill-row"><span>Skill 3</span><span class="pct">90%</span></div><div class="track"><i style="width:90%"></i></div></div>
  </div>

  <footer class="slide-footer">
    <div class="contact" style="left:58px"><span class="ico"><svg><use href="#pin"/></svg></span><div><b>Address:</b><span>Lorem ipsum dolor sit amet.</span></div></div>
    <div class="contact" style="left:355px"><span class="ico"><svg><use href="#phone"/></svg></span><div><b>Contact No:</b><span>Lorem ipsum dolor sit amet.</span></div></div>
    <div class="contact" style="left:629px"><span class="ico"><svg><use href="#mail"/></svg></span><div><b>Email:</b><span>www.yourmail.com</span></div></div>
  </footer>
</section>

<!-- Work experience detail -->
<section class="slide work-detail" style="top:1911px">
  <div class="abs" style="left:0;top:0;width:45px;bottom:0;background:var(--ink)"></div>
  <div class="wordmark" style="left:71px;top:24px;font-size:28px">korvane</div>
  <div class="photo" role="img" aria-label="Profile portrait" style="left:57px;top:94px;width:130px;height:130px"></div>
  <div class="hello" style="left:236px;top:74px">HELLO I AM,</div>
  <div class="hello-rule" style="left:236px;top:104px"></div>
  <div class="name" style="left:234px;top:118px">Aldric<br>Venn</div>
  <div class="role" style="left:236px;top:204px">Korvane Lead</div>
  <div class="socials" style="left:236px;top:239px" aria-label="Social profiles"><i></i><i></i><i></i></div>

  <div class="card" style="left:80px;top:272px;width:442px;height:187px">
    <div class="card-title" style="left:31px;top:14px">About Me</div>
    <div class="body" style="left:31px;top:42px;width:395px">Lorem ipsum dolor sit amet, consectetuer adipiscing elit. Maecenas porttitor congue massa. Fusce posuere, magna sed pulvinar ultricies, purus lectus malesuada libero, sit amet commodo magna eros quis urna.</div>
    <div class="body" style="left:31px;top:125px;width:395px">Lorem ipsum dolor sit amet, consectetuer adipiscing elit. Maecenas porttitor congue massa.</div>
  </div>

  <div class="abs" style="left:542px;top:38px;width:369px;height:30px;background:var(--panel-dark);border-radius:3px;font-size:17px;font-weight:600;line-height:30px;padding-left:9px">Work Experience Summary</div>
  <div class="abs" style="left:560px;top:78px;font-size:16px;font-weight:600">JOB TITLE</div>
  <div class="abs blue" style="right:45px;top:78px;font-size:15px;font-weight:500">2016–2018</div>
  <div class="abs small-blue" style="left:560px;top:104px;font-size:13px">Company Name</div>
  <div class="body" style="left:560px;top:124px;width:345px">Lorem ipsum dolor sit amet, consectetuer adipiscing elit. Maecenas porttitor congue massa. Lorem ipsum dolor sit amet, consectetuer adipiscing elit. Lorem ipsum dolor sit amet, consectetuer adipiscing elit.</div>
  <div class="abs" style="left:560px;top:205px;font-size:13px;color:#cfcfcf">Accomplishments:</div>
  <div class="bullet" style="left:560px;top:225px;width:345px">Lorem ipsum dolor sit amet, consectetuer adipiscing elit. Maecenas porttitor congue massa.</div>
  <div class="bullet" style="left:560px;top:272px;width:345px">Lorem ipsum dolor sit amet, consectetuer adipiscing elit. Maecenas porttitor congue massa.</div>
  <div class="bullet" style="left:560px;top:319px;width:345px">Lorem ipsum dolor sit amet, consectetuer adipiscing elit. Maecenas porttitor congue massa.</div>
  <div class="skill big" style="left:560px;width:329px;top:369px"><div class="skill-row"><span>Scope of work</span><span class="pct">70%</span></div><div class="track"><i style="width:70%"></i></div></div>
  <div class="skill big" style="left:560px;width:329px;top:413px"><div class="skill-row"><span>Achievements</span><span class="pct">90%</span></div><div class="track"><i style="width:90%"></i></div></div>

  <footer class="slide-footer">
    <div class="contact" style="left:58px"><span class="ico"><svg><use href="#pin"/></svg></span><div><b>Address:</b><span>Lorem ipsum dolor sit amet.</span></div></div>
    <div class="contact" style="left:355px"><span class="ico"><svg><use href="#phone"/></svg></span><div><b>Contact No:</b><span>Lorem ipsum dolor sit amet.</span></div></div>
    <div class="contact" style="left:629px"><span class="ico"><svg><use href="#mail"/></svg></span><div><b>Email:</b><span>www.yourmail.com</span></div></div>
  </footer>
</section>

<!-- Education and competences -->
<section class="slide competences" style="top:2505px">
  <div class="card" style="left:20px;top:15px;width:266px;height:469px">
    <div class="card-head" style="top:6px">Work Experience</div>
    <div class="abs small-blue" style="left:12px;top:57px">Company Name</div><div class="abs" style="right:12px;top:57px;font-size:11px;color:var(--text)">2016-2018</div>
    <div class="body" style="left:12px;top:74px;width:245px">Lorem ipsum dolor sit amet, consectetuer adipiscing elit.</div>
    <div class="abs small-blue" style="left:12px;top:132px">Company Name</div><div class="abs" style="right:12px;top:132px;font-size:11px;color:var(--text)">2019-2020</div>
    <div class="body" style="left:12px;top:149px;width:245px">Lorem ipsum dolor sit amet, consectetuer adipiscing elit.</div>
    <div class="abs small-blue" style="left:12px;top:207px">Company Name</div><div class="abs" style="right:12px;top:207px;font-size:11px;color:var(--text)">2021-2023</div>
    <div class="body" style="left:12px;top:224px;width:245px">Lorem ipsum dolor sit amet, consectetuer adipiscing elit.</div>
    <div class="abs small-blue" style="left:12px;top:282px">Company Name</div><div class="abs" style="right:12px;top:282px;font-size:11px;color:var(--text)">2024-2025</div>
    <div class="body" style="left:12px;top:299px;width:245px">Lorem ipsum dolor sit amet, consectetuer adipiscing elit.</div>
    <div class="card-head" style="top:330px">Skill</div>
    <div class="skill" style="left:12px;right:12px;top:370px"><div class="skill-row"><span>Skill 1</span><span class="pct">70%</span></div><div class="track"><i style="width:70%"></i></div></div>
    <div class="skill" style="left:12px;right:12px;top:398px"><div class="skill-row"><span>Skill 2</span><span class="pct">50%</span></div><div class="track"><i style="width:50%"></i></div></div>
    <div class="skill" style="left:12px;right:12px;top:426px"><div class="skill-row"><span>Skill 3</span><span class="pct">90%</span></div><div class="track"><i style="width:90%"></i></div></div>
  </div>

  <div class="wordmark" style="left:300px;width:330px;top:24px;text-align:center;font-size:28px">korvane</div>
  <div class="photo" role="img" aria-label="Profile portrait" style="left:400px;top:92px;width:130px;height:130px"></div>
  <div class="dash" style="left:445px;top:261px;width:42px"></div>
  <div class="name" style="left:300px;width:330px;top:270px;text-align:center">Aldric Venn</div>
  <div class="role" style="left:300px;width:330px;top:313px;text-align:center;font-size:15px">Korvane Lead</div>
  <div class="socials" style="left:437px;top:341px" aria-label="Social profiles"><i></i><i></i><i></i></div>
  <div class="card" style="left:304px;top:367px;width:328px;height:117px">
    <div class="card-title" style="left:0;right:0;top:3px;text-align:center">About Me</div>
    <div class="body" style="left:12px;right:12px;top:26px;text-align:center">Lorem ipsum dolor sit amet, consectetuer adipiscing elit. Maecenas porttitor congue massa. Fusce posuere, magna sed pulvinar ultricies, purus lectus malesuada libero, sit amet</div>
  </div>

  <div class="card" style="left:648px;top:15px;width:274px;height:469px">
    <div class="card-head" style="top:6px">Achievements</div>
    <div class="abs" style="left:12px;top:52px;font-size:11px;color:var(--text)">2021- <span class="blue">Achievements I</span></div>
    <div class="bullet" style="left:12px;top:70px;width:250px">Lorem ipsum dolor sit amet, consectetuer adipiscing elit.</div>
    <div class="abs" style="left:12px;top:124px;font-size:11px;color:var(--text)">2022- <span class="blue">Achievements I</span></div>
    <div class="bullet" style="left:12px;top:142px;width:250px">Lorem ipsum dolor sit amet, consectetuer adipiscing elit.</div>
    <div class="abs" style="left:12px;top:195px;font-size:11px;color:var(--text)">2023- <span class="blue">Achievements I</span></div>
    <div class="bullet" style="left:12px;top:213px;width:250px">Lorem ipsum dolor sit amet, consectetuer adipiscing elit.</div>
    <div class="card-head" style="top:252px">Education</div>
    <div class="abs" style="left:12px;top:293px;font-size:11px;line-height:14px;color:var(--text)">2016-<br>2018</div>
    <div class="abs small-blue" style="left:60px;top:291px">Master Degree</div>
    <div class="body" style="left:60px;top:305px">Name of the university/college</div>
    <div class="abs" style="left:12px;top:335px;font-size:11px;line-height:14px;color:var(--text)">2014-<br>2015</div>
    <div class="abs small-blue" style="left:60px;top:333px">Bachelor Degree</div>
    <div class="body" style="left:60px;top:347px">Name of the university/college</div>
    <div class="card-head" style="top:376px">Hobbies</div>
    <div class="hobbies" style="left:6px;top:416px;width:262px">
      <div class="hobby" style="width:66px"><svg><use href="#pen"/></svg>Writing</div>
      <div class="hobby" style="width:66px"><svg><use href="#film"/></svg>Movies</div>
      <div class="hobby" style="width:66px"><svg><use href="#ball"/></svg>Sport</div>
      <div class="hobby" style="width:64px"><svg><use href="#book"/></svg>Reading</div>
    </div>
  </div>

  <footer class="slide-footer">
    <div class="contact" style="left:58px"><span class="ico"><svg><use href="#pin"/></svg></span><div><b>Address:</b><span>Lorem ipsum dolor sit amet.</span></div></div>
    <div class="contact" style="left:355px"><span class="ico"><svg><use href="#phone"/></svg></span><div><b>Contact No:</b><span>Lorem ipsum dolor sit amet.</span></div></div>
    <div class="contact" style="left:629px"><span class="ico"><svg><use href="#mail"/></svg></span><div><b>Email:</b><span>www.yourmail.com</span></div></div>
  </footer>
</section>

<!-- Work summary with metrics -->
<section class="slide work-metrics" style="top:3097px">
  <div class="wordmark" style="left:71px;top:24px;font-size:28px">korvane</div>
  <div class="photo" role="img" aria-label="Profile portrait" style="left:54px;top:87px;width:130px;height:130px"></div>
  <div class="hello" style="left:236px;top:76px">HELLO I AM,</div>
  <div class="hello-rule" style="left:236px;top:106px"></div>
  <div class="name" style="left:234px;top:119px">Aldric<br>Venn</div>
  <div class="role" style="left:236px;top:205px">Korvane Lead</div>
  <div class="socials" style="left:236px;top:240px" aria-label="Social profiles"><i></i><i></i><i></i></div>

  <div class="card" style="left:455px;top:76px;width:443px;height:173px">
    <div class="card-title" style="left:32px;top:11px">About Me</div>
    <div class="body" style="left:32px;top:39px;width:395px">Lorem ipsum dolor sit amet, consectetuer adipiscing elit. Maecenas porttitor congue massa. Fusce posuere, magna sed pulvinar ultricies, purus lectus malesuada libero, sit amet commodo magna eros quis urna.</div>
    <div class="body" style="left:32px;top:122px;width:395px">Lorem ipsum dolor sit amet, consectetuer adipiscing elit. Maecenas porttitor congue massa.</div>
  </div>

  <div class="abs" style="left:39px;top:270px;width:866px;height:33px;background:var(--panel-dark);border-radius:3px;font-size:17px;font-weight:600;line-height:33px;padding-left:10px">Work Experience Summary</div>
  <div class="abs" style="left:48px;top:313px;font-size:16px;font-weight:600">JOB TITLE</div>
  <div class="abs blue" style="right:46px;top:313px;font-size:15px;font-weight:500">2016–2018</div>
  <div class="abs small-blue" style="left:48px;top:338px;font-size:13px">Company Name</div>
  <div class="body" style="left:48px;top:358px;width:300px">Lorem ipsum dolor sit amet, consectetuer adipiscing elit. Maecenas porttitor congue massa. Lorem ipsum dolor sit amet, consectetuer adipiscing elit. Lorem ipsum dolor sit amet, consectetuer adipiscing elit.</div>
  <div class="abs small-blue" style="left:388px;top:338px;font-size:13px">Accomplishments:</div>
  <div class="bullet" style="left:388px;top:358px;width:230px">Lorem ipsum dolor sit amet, consectetuer adipiscing elit. Maecenas porttitor congue massa.</div>
  <div class="bullet" style="left:388px;top:422px;width:230px">Lorem ipsum dolor sit amet, consectetuer adipiscing elit.</div>

  <div class="donut" style="left:644px;top:362px">
    <svg viewBox="0 0 72 72"><circle cx="36" cy="36" r="31" fill="none" stroke="#5a5a5a" stroke-width="5"/><circle cx="36" cy="36" r="31" fill="none" stroke="var(--blue)" stroke-width="5" stroke-dasharray="97.4 194.8" transform="rotate(-90 36 36)"/></svg>
    <div class="val">50%</div><div class="cap">Lorem ipsum</div>
  </div>
  <div class="donut" style="left:740px;top:362px">
    <svg viewBox="0 0 72 72"><circle cx="36" cy="36" r="31" fill="none" stroke="#5a5a5a" stroke-width="5"/><circle cx="36" cy="36" r="31" fill="none" stroke="var(--blue)" stroke-width="5" stroke-dasharray="87.7 194.8" transform="rotate(-90 36 36)"/></svg>
    <div class="val">45%</div><div class="cap">Lorem ipsum</div>
  </div>
  <div class="donut" style="left:833px;top:362px">
    <svg viewBox="0 0 72 72"><circle cx="36" cy="36" r="31" fill="none" stroke="#5a5a5a" stroke-width="5"/><circle cx="36" cy="36" r="31" fill="none" stroke="var(--blue)" stroke-width="5" stroke-dasharray="165.6 194.8" transform="rotate(-90 36 36)"/></svg>
    <div class="val">85%</div><div class="cap">Lorem ipsum</div>
  </div>

  <footer class="slide-footer">
    <div class="contact" style="left:58px"><span class="ico"><svg><use href="#pin"/></svg></span><div><b>Address:</b><span>Lorem ipsum dolor sit amet.</span></div></div>
    <div class="contact" style="left:355px"><span class="ico"><svg><use href="#phone"/></svg></span><div><b>Contact No:</b><span>Lorem ipsum dolor sit amet.</span></div></div>
    <div class="contact" style="left:629px"><span class="ico"><svg><use href="#mail"/></svg></span><div><b>Email:</b><span>www.yourmail.com</span></div></div>
  </footer>
</section>

</body>
</html>
```